Business Card for a recruitment agency specializing in engineers and geeks.

I am looking to create Business Card Design for my company.
That
## Company name:
Vornplick Inc.
Vornplick is a term coined from the following concepts.
1. geek + engineer
2. geek utopia
## Company Description:
The concept of the company is to be a recruitment agency that creates a paradise for geeky engineers. We want to be a place where engineers can have more freedom and ideal career support.
# Target.
The noun itself is often given to companies that want to hire engineers, geeks, and IT-related personnel, so it would be nice to get the impression that this company seems to have good engineers and IT personnel. There are many occasions where I meet with the human resources department, president, or senior management and give it to them.
# Atmosphere
We are happy with simplicity, but with an impact that will help people remember the company. The logo is based on a dinosaur that does programming, so it should be somewhat playful, but since it will basically be used in a business setting, please don't make it too silly.
# About the logo
See the attached files. The company logo represents our engineers smiling upward because of our work, with the motif of a dinosaur doing programming.
## Color
We will leave the color scheme to you, but since the logo is in black and white, colors with such a taste would fit well.
## file format
ai, psd, png, svg
Industry/Entity Type
human resource and employment agency
Contact Information for Business Card
Company name, address, email, tel, URL,logo
Colors
Designer to choose colors to be used in the design.
Look and feel
Each slider illustrates characteristics of the customer's brand and the style your logo design should communicate.

```html
<!DOCTYPE html>
<html lang="en">
<head>
<meta charset="utf-8">
<title>Vornplick Business Card</title>
<link rel="stylesheet" href="https://fonts.googleapis.com/css2?family=Montserrat:wght@400;500;700&display=swap">
<style>
  :root {
    --page-bg: #eceded;
    --card-front: #ffffff;
    --ink: #1c1c1c;
    --ink-soft: #333333;
    --rule: #3a3a3a;
    --card-back: #313131;
    --pattern-dark: #262626;
    --pattern-light: #3d3d3d;
    --white: #ffffff;
  }
  * { margin: 0; padding: 0; box-sizing: border-box; }
  html, body {
    width: 1054px;
    height: 1200px;
    overflow: hidden;
    background: var(--page-bg);
    font-family: "Montserrat", Arial, sans-serif;
  }
  .canvas { position: relative; width: 1054px; height: 1200px; }

  .card-front {
    position: absolute;
    left: 73px; top: 63px;
    width: 909px; height: 518px;
    background: var(--card-front);
    overflow: hidden;
  }
  .card-front .bottom-band {
    position: absolute; left: 0; right: 0; bottom: 0;
    height: 10px; background: var(--ink);
  }
  .brand {
    position: absolute; left: 49px; top: 76px;
    display: flex; align-items: center; gap: 16px;
  }
  .brand-square {
    width: 46px; height: 46px;
    border: 6px solid var(--ink);
    border-radius: 6px;
  }
  .brand-name {
    font-weight: 500; font-size: 46px; color: var(--ink);
    letter-spacing: 0.5px; line-height: 1;
  }
  .person-name {
    position: absolute; left: 49px; top: 288px;
    font-weight: 700; font-size: 41px; color: var(--ink-soft);
    letter-spacing: -0.5px; line-height: 1;
  }
  .person-title {
    position: absolute; left: 49px; top: 336px;
    font-weight: 400; font-size: 22px; color: var(--ink-soft);
    letter-spacing: 0.6px;
  }
  .divider {
    position: absolute; left: 49px; top: 375px;
    width: 811px; height: 2px; background: var(--rule);
  }
  .contact-list {
    position: absolute; left: 49px; top: 390px;
    list-style: none;
  }
  .contact-list li {
    display: flex; align-items: center; gap: 18px;
    font-size: 22px; color: var(--ink-soft);
    height: 33px;
  }
  .contact-list svg { width: 22px; height: 22px; flex: none; }
  .address {
    position: absolute; right: 47px; top: 412px;
    text-align: right; font-size: 22px; color: var(--ink-soft);
    line-height: 29px;
  }

  .card-back {
    position: absolute;
    left: 79px; top: 628px;
    width: 909px; height: 521px;
    background: var(--card-back);
    overflow: hidden;
  }
  .back-pattern {
    position: absolute; inset: 0;
    background: linear-gradient(90deg, var(--pattern-dark) 0%, var(--card-back) 55%, var(--pattern-light) 100%);
  }
  .back-brand {
    position: absolute; left: 589px; top: 313px;
    transform: translate(-50%, -50%);
    display: flex; align-items: center; gap: 14px;
    white-space: nowrap;
  }
  .back-brand-square {
    width: 58px; height: 58px;
    border: 7px solid var(--white);
    border-radius: 7px;
  }
  .back-brand-name {
    font-weight: 500; font-size: 34px; color: var(--white);
    letter-spacing: 0.5px; line-height: 1;
  }
</style>
</head>
<body>
<div class="canvas">
  <section class="card-front">
    <div class="brand">
      <div class="brand-square"></div>
      <span class="brand-name">Vornplick</span>
    </div>

    <h1 class="person-name">DORIAN HALVEK</h1>
    <p class="person-title">Managing Director</p>
    <div class="divider"></div>

    <ul class="contact-list">
      <li>
        <svg viewBox="0 0 24 24" aria-hidden="true"><path d="M6.6 10.8a15 15 0 0 0 6.6 6.6l2.2-2.2c.3-.3.7-.4 1-.2 1.1.4 2.3.6 3.6.6.6 0 1 .4 1 1V20c0 .6-.4 1-1 1A17 17 0 0 1 3 4c0-.6.4-1 1-1h3.5c.6 0 1 .4 1 1 0 1.3.2 2.5.6 3.6.1.3 0 .7-.2 1z" fill="#1c1c1c"/></svg>
        <span>031-555 208 417</span>
      </li>
      <li>
        <svg viewBox="0 0 24 24" aria-hidden="true"><rect x="2" y="5" width="20" height="14" fill="#1c1c1c"/><path d="M2 5l10 8 10-8" fill="none" stroke="#fff" stroke-width="1.6"/></svg>
        <span>hello@vornplick.example</span>
      </li>
      <li>
        <svg viewBox="0 0 24 24" aria-hidden="true"><circle cx="12" cy="12" r="10" fill="#1c1c1c"/><path d="M2 12h20M12 2c3 3 3 17 0 20M12 2c-3 3-3 17 0 20" fill="none" stroke="#fff" stroke-width="1.4"/></svg>
        <span>www.vornplick.example</span>
      </li>
    </ul>

    <p class="address">58, Larkmoor Lane<br>Elsworth Bay, 70318</p>
    <div class="bottom-band"></div>
  </section>

  <section class="card-back">
    <div class="back-pattern" role="img" aria-label="Embossed repeating brand pattern in dark grey tones"></div>
    <div class="back-brand">
      <div class="back-brand-square"></div>
      <span class="back-brand-name">Vornplick</span>
    </div>
  </section>
</div>
</body>
</html>
```